2021 Personalized Vision Poster

A beautiful, pleasing design for my 2021 vision poster. Looking probably for an infographic. Open to shortening the wording used if able. As you will notice, each color represents a different category. Let me know if you need more details. The title of each section are mostly listed, but starting with the upper left with “my primary question” going counter-clockwise: my primary question, away values and rules, life purpose, power values (red), toward values and rules, top 4 goals for 2021 (middle), and relationship vision (middle). Basically, I’m just looking for a nice font and different formatting for my words.

Requirements
Must have
• All of the sections with a majority of the words used.
Nice to have
• Infographic would be nice, if possible. More concerned with a beautiful layout of words already expressed.
Should not have
• A complete reworking of the words used.

```html
<!DOCTYPE html>
<html lang="en">
<head>
<meta charset="utf-8">
<title>2021 Live Courageously – Vision Poster</title>
<link rel="stylesheet" href="https://fonts.googleapis.com/css2?family=Sniglet:wght@400;800&family=Patrick+Hand&family=Grenze+Gotisch:wght@600&display=swap">
<style>
  :root {
    --bg: #000000;
    --panel: #3d393b;
    --frame: #9b9094;
    --ink: #0d0b0c;
    --title: #ffffff;
    --font-title: "Sniglet", sans-serif;
    --font-body: "Patrick Hand", cursive;
    --font-name: "Grenze Gotisch", serif;
  }
  html, body {
    margin: 0;
    padding: 0;
    width: 1200px;
    height: 848px;
    overflow: hidden;
    background: var(--bg);
  }
  .poster {
    display: block;
    width: 1200px;
    height: 848px;
  }
  .frame { fill: var(--frame); }
  .panel { fill: var(--panel); }
  .divider { fill: none; stroke: var(--frame); stroke-width: 10; }
  .hub { fill: var(--frame); }
  .poster-title {
    font-family: var(--font-title);
    font-weight: 800;
    font-size: 44px;
    fill: var(--title);
  }
  .purpose {
    font-family: var(--font-title);
    font-weight: 400;
    font-size: 14.5px;
    fill: var(--title);
  }
  .body-text {
    font-family: var(--font-body);
    fill: var(--ink);
  }
  .heading {
    font-size: 17px;
    text-decoration: underline;
  }
  .line { font-size: 13px; }
  .line-small { font-size: 10.5px; }
  .line-strong { font-size: 15px; font-weight: bold; }
  .question { font-size: 16px; }
  .vision-word { font-size: 18px; }
  .goal { font-size: 18px; }
  .power-heading { font-size: 11px; text-decoration: underline; }
  .power-line { font-size: 9px; }
  .owner-name {
    font-family: var(--font-name);
    font-weight: 600;
    font-size: 40px;
    fill: var(--ink);
  }
</style>
</head>
<body>
<svg class="poster" viewBox="0 0 842 595" xmlns="http://www.w3.org/2000/svg">

  <text class="poster-title" x="421" y="62" text-anchor="middle">2021 LIVE COURAGEOUSLY</text>

  <g class="fan">
    <path class="frame" d="M9 510 A412 412 0 0 1 833 510 Z"/>
    <path class="panel" d="M21 510 A400 400 0 0 1 821 510 Z"/>
    <path class="divider" d="M215.9 304.9 A290 290 0 0 1 626.1 304.9"/>
    <path class="divider" d="M286.6 375.6 A190 190 0 0 1 611 510"/>
    <line class="divider" x1="138.2" y1="227.2" x2="355.9" y2="444.9"/>
    <line class="divider" x1="703.8" y1="227.2" x2="486.1" y2="444.9"/>
    <path class="hub" d="M329 510 A92 92 0 0 1 513 510 Z"/>
  </g>

  <g class="body-text primary-question" text-anchor="middle">
    <text class="question" x="421" y="160">"How can I be even more grateful for the love</text>
    <text class="question" x="421" y="177">in my heart for God, myself &amp; others?"</text>
    <text class="question" x="421" y="194">–My Primary Question</text>
  </g>

  <g class="body-text relationship-vision" text-anchor="middle">
    <text class="heading" x="421" y="240">Relationship Vision:</text>
    <text class="vision-word" x="421" y="264">Love  –  Respect  –  Courage</text>
    <text class="vision-word" x="421" y="284">Desire  –  Fun  –  Flirty</text>
    <text class="vision-word" x="421" y="304">Romantic</text>
  </g>

  <g class="body-text top-goals" text-anchor="middle">
    <text class="heading" x="421" y="350">TOP 4:</text>
    <text class="goal" x="421" y="373">1. Rental   2. 175 lbs</text>
    <text class="goal" x="421" y="393">3. Team   4. $250K</text>
  </g>

  <g class="owner" text-anchor="middle">
    <text class="owner-name" x="421" y="458">Sam</text>
    <text class="owner-name" x="421" y="500">R.</text>
  </g>

  <g class="body-text away-values" text-anchor="middle" transform="translate(421 510) rotate(-67.5)">
    <text class="heading" x="0" y="-376">Away Values &amp; Rules:</text>
    <text class="line" x="0" y="-358">Only if I were to avoid...</text>
    <text class="line-strong" x="0" y="-340">–Consistent, unrighteous anger</text>
    <text class="line-small" x="0" y="-324">–Consistent, debilitating illusion of failure</text>
    <text class="line-strong" x="0" y="-306">–Consistent, debilitating anxiety</text>
    <text class="line" x="0" y="-289">Instead of...</text>
    <text class="line" x="0" y="-272">–Knowing that I alone have the</text>
    <text class="line" x="0" y="-256">power to choose to be angry</text>
    <text class="line" x="0" y="-240">–Realizing God has made me a</text>
    <text class="line" x="0" y="-224">conqueror (I will not fail)</text>
    <text class="line" x="0" y="-208">–Realizing God has</text>
    <text class="line" x="0" y="-192">given me all inner</text>
    <text class="line" x="0" y="-176">peace I need</text>
  </g>

  <g class="body-text towards-values" text-anchor="middle" transform="translate(421 510) rotate(67.5)">
    <text class="heading" x="0" y="-376">Towards Values &amp; Rules:</text>
    <text class="line-strong" x="0" y="-358">Anytime I am...</text>
    <text class="line" x="0" y="-341">–Giving myself and serve others, OR –Accepting</text>
    <text class="line" x="0" y="-325">love from God or others, OR –Allowing myself</text>
    <text class="line" x="0" y="-309">to stay present, OR –Doing something even</text>
    <text class="line" x="0" y="-293">when scary, OR –Choosing to put myself</text>
    <text class="line" x="0" y="-277">first, OR –Practicing vulnerability, OR</text>
    <text class="line-small" x="0" y="-263">–Taking actions consistent with my identity, OR</text>
    <text class="line-strong" x="0" y="-245">–MOVING MY BODY!</text>
  </g>

  <g class="body-text power-values" text-anchor="middle" transform="translate(421 510) rotate(67.5)">
    <text class="power-heading" x="0" y="-165">POWER VALUES:</text>
    <text class="power-line" x="0" y="-150">–Courage –Love–</text>
    <text class="power-line" x="0" y="-137">–Joy –Presence–</text>
  </g>

  <g class="life-purpose" text-anchor="middle">
    <text class="purpose" x="421" y="552">The purpose of my life is to be loving, courageous, and fun! I seek adventure, laughter, and play, and live</text>
    <text class="purpose" x="421" y="573">in God's identity for me.</text>
  </g>
</svg>
</body>
</html>
```